Statement of Capabilities

We are looking for a fresh new stationary (Word Template) and a new look for our statement of capabilities....logo must be the same.

We are an electrical / lighting contractor-

www.BrightfieldServicing.com

Target Market(s)

B2B and government agencies

Industry/Entity Type

Electrical

Colors
eb1f27
0655a3

Requirements
Must have
• LOGO

```html
<!DOCTYPE html>
<html lang="en">
<head>
<meta charset="utf-8">
<title>Brightfield Servicing Incorporated – Letterhead</title>
<link rel="stylesheet" href="https://fonts.googleapis.com/css2?family=Arimo:wght@400;700&display=swap">
<style>
  :root {
    --brand-red: #eb1f27;
    --brand-blue: #0655a3;
    --ink: #2b2b2b;
    --footer-grey: #eeeeee;
    --faint-mark: #f2b8a4;
    --page: #ffffff;
  }
  * { margin: 0; padding: 0; box-sizing: border-box; }
  html, body {
    width: 927px;
    height: 1200px;
    overflow: hidden;
    background: var(--page);
  }
  .letterhead {
    position: relative;
    width: 927px;
    height: 1200px;
    background: var(--page);
    font-family: "Arimo", Arial, sans-serif;
  }
  .rule { position: absolute; }
  .rule--top-blue {
    left: 22px; top: 9px; width: 891px; height: 6px;
    background: var(--brand-blue);
  }
  .rule--header-red {
    left: 314px; top: 121px; width: 591px; height: 5px;
    background: var(--brand-red);
  }
  .company-name {
    position: absolute;
    left: 52px; top: 30px;
    width: 245px;
    color: var(--brand-red);
    font-weight: 700;
    text-align: center;
    line-height: 1;
  }
  .company-name span { display: block; }
  .company-name .line-1 { font-size: 31px; letter-spacing: 0.5px; }
  .company-name .line-2 { font-size: 31px; margin-top: 6px; letter-spacing: 1px; }
  .company-name .line-3 { font-size: 15px; margin-top: 8px; letter-spacing: 0.5px; }

  .contact {
    position: absolute;
    left: 470px; top: 60px; width: 448px;
    text-align: center;
    color: var(--ink);
    font-size: 16px;
    line-height: 20px;
  }

  .footer {
    position: absolute;
    left: 0; top: 1058px; width: 927px; height: 142px;
    background: var(--footer-grey);
  }
  .footer__red {
    position: absolute; left: 0; top: 0; width: 100%; height: 7px;
    background: var(--brand-red);
  }
  .footer__gap {
    position: absolute; left: 0; top: 7px; width: 100%; height: 5px;
    background: var(--page);
  }
  .footer__blue {
    position: absolute; left: 0; top: 12px; width: 100%; height: 7px;
    background: var(--brand-blue);
  }
  .footer__web {
    position: absolute; left: 104px; top: 71px;
    color: var(--brand-blue);
    font-size: 18px;
  }
  .footer__name {
    position: absolute;
    left: 612px; top: 36px; width: 250px;
    color: var(--faint-mark);
    font-weight: 700;
    text-align: center;
    line-height: 1;
  }
  .footer__name span { display: block; }
  .footer__name .line-1 { font-size: 31px; }
  .footer__name .line-2 { font-size: 31px; margin-top: 6px; }
  .footer__name .line-3 { font-size: 15px; margin-top: 8px; }
</style>
</head>
<body>
  <div class="letterhead">
    <div class="rule rule--top-blue"></div>

    <div class="company-name">
      <span class="line-1">BRIGHTFIELD</span>
      <span class="line-2">SERVICING</span>
      <span class="line-3">INCORPORATED</span>
    </div>

    <p class="contact">
      415 Harbor Ave Suite B, Glenmoor Maryland 21044<br>
      Phone 877-555-0142&nbsp; - &nbsp;Fax:&nbsp; 877-555-0143
    </p>

    <div class="rule rule--header-red"></div>

    <footer class="footer">
      <div class="footer__red"></div>
      <div class="footer__gap"></div>
      <div class="footer__blue"></div>
      <p class="footer__web">www.BrightfieldServicing.com</p>
      <div class="footer__name">
        <span class="line-1">BRIGHTFIELD</span>
        <span class="line-2">SERVICING</span>
        <span class="line-3">INCORPORATED</span>
      </div>
    </footer>
  </div>
</body>
</html>
```